Pelican Crest landing page design

We need a landing page designed for an ecommerce website that sales fresh US domestic shrimp from the Gulf of Mexico and ships them direct to the consumer "From Our Shore To Your Door". For the landing page, we would like customers to be able to place an order and or inquire further about our product as well as links to social media. The company logo is attached

1 page

```html
<!DOCTYPE html>
<html lang="en">
<head>
<meta charset="utf-8">
<title>Pelican Crest</title>
<link href="https://fonts.googleapis.com/css2?family=Montserrat:wght@400;500;600;700&display=swap" rel="stylesheet">
<style>
:root{
  --orange:#ee8a4b;
  --orange-dark:#d6743d;
  --blue:#5bbde8;
  --star:#6cc46b;
  --ink:#444;
  --muted:#777;
  --white:#fff;
  --sea:#2e9aa0;
  --sand:#e9e6e0;
}
*{margin:0;padding:0;box-sizing:border-box}
html,body{width:820px;height:1200px;overflow:hidden}
body{font-family:'Montserrat',sans-serif;color:var(--ink);background:var(--white);position:relative}
.abs{position:absolute}
/* header */
.header{left:0;top:0;width:820px;height:42px;background:var(--white)}
.brand{left:158px;top:6px;display:flex;align-items:center;gap:6px}
.brand-mark{width:30px;height:30px;border:1.5px solid var(--orange);border-radius:50%}
.brand-name{font-size:13px;font-weight:600;color:#6b6b6b;letter-spacing:.5px}
.nav{top:16px;font-size:8.5px;color:#666}
.nav.active{border-bottom:1px solid var(--orange);padding:0 2px 3px;left:327px}
.cart{left:587px;top:15px}
.signup{left:610px;top:12px;width:53px;height:19px;border:1.2px solid var(--orange);border-radius:3px;color:var(--orange);font-size:7px;font-weight:500;display:flex;align-items:center;justify-content:center;letter-spacing:.5px}
/* hero */
.hero{left:0;top:42px;width:820px;height:300px;background:linear-gradient(165deg,#3f8f97 0%,#2e9fa4 38%,#6bbcb8 58%,#e5e3dc 70%,#ecebe6 100%)}
.hero-title{left:0;top:150px;width:820px;text-align:center;color:var(--white);font-size:22px;font-weight:700}
.hero-sub{left:0;top:180px;width:820px;text-align:center;color:var(--white);font-size:10px;font-weight:600;letter-spacing:.3px}
.btn{background:var(--orange);color:var(--white);font-size:7px;font-weight:500;letter-spacing:.4px;display:flex;align-items:center;justify-content:center;width:85px;height:21px}
/* how it works */
.section-title{left:0;width:820px;text-align:center;font-size:12px;font-weight:600;color:#4a4a4a;letter-spacing:.5px}
.step-icon{width:69px;height:69px;border:1.3px solid var(--blue);border-radius:50%;display:flex;align-items:center;justify-content:center}
.step-title{font-size:12px;font-weight:500;color:#444;letter-spacing:.3px}
.step-text{font-size:7px;color:var(--muted);line-height:8.4px;margin-top:4px}
.step.right{text-align:right}
/* love panel */
.food{left:0;top:682px;width:410px;height:232px;background:radial-gradient(circle at 52% 55%,#e98a5c 0%,#b46a4a 25%,#5d6b3c 55%,#3a3a2a 80%,#d8d8d0 100%)}
.love{left:410px;top:682px;width:410px;height:232px;background:var(--orange);color:var(--white);padding:22px 12px 0 12px}
.love h2{font-size:12px;font-weight:700;letter-spacing:.3px;margin-bottom:14px}
.love p{font-size:7px;line-height:10.3px;margin-bottom:10px;width:240px}
/* reviews */
.review{width:120px;text-align:center;top:963px}
.stars{display:flex;justify-content:center;gap:2px;margin-bottom:3px}
.review-text{font-size:7px;line-height:8.2px;color:#555}
.review-name{font-size:7px;font-weight:600;color:#444;margin-top:3px}
.arrow{top:990px;font-size:13px;color:#888}
.more{left:0;width:820px;top:1043px;text-align:center;font-size:7px;color:#555}
.more span{color:var(--blue);font-size:5px}
/* footer */
.footer{left:0;top:1072px;width:820px;height:106px;background:var(--orange);color:var(--white)}
.foot-links{left:192px;top:22px;font-size:7.5px;line-height:13.6px}
.foot-title{font-size:8px;font-weight:600}
.social{left:330px;top:20px;width:160px;text-align:center}
.social-row{display:flex;justify-content:space-between;margin-top:7px;padding:0 7px}
.social-item{width:34px;height:34px;border-radius:50%;background:var(--white);color:var(--orange);font-size:5.5px;font-weight:600;display:flex;align-items:center;justify-content:center}
.contact{left:567px;top:22px;width:60px}
.contact p{font-size:7px;line-height:8px;margin-top:5px}
.bottom{left:0;top:1178px;width:820px;height:22px;background:var(--orange-dark);color:var(--white);font-size:6px}
</style>
</head>
<body>
<header class="abs header">
  <div class="abs brand"><span class="brand-mark"></span><span class="brand-name">Pelican Crest</span></div>
  <span class="abs nav active">Home</span>
  <span class="abs nav" style="left:370px">How It Works</span>
  <span class="abs nav" style="left:442px">Menu</span>
  <span class="abs nav" style="left:482px">About</span>
  <svg class="abs cart" width="12" height="11" viewBox="0 0 12 11" fill="none" stroke="#999" stroke-width="1"><path d="M0.5 1h2l1.5 6h6l1.3-4.3H3.2"/><circle cx="4.5" cy="9.3" r=".9"/><circle cx="9" cy="9.3" r=".9"/></svg>
  <div class="abs signup">SIGN UP</div>
</header>

<section class="abs hero" role="img" aria-label="Aerial photo of turquoise gulf water meeting a white sand beach with a few people walking"></section>
<h1 class="abs hero-title">From our shore to your door</h1>
<p class="abs hero-sub">Fresh Shrimp delivered directly at your doorstep.</p>
<div class="abs btn" style="left:368px;top:207px">GET STARTED</div>

<h2 class="abs section-title" style="top:360px">HOW IT WORKS</h2>

<div class="abs step-icon" style="left:410px;top:393px">
  <svg width="34" height="26" viewBox="0 0 34 26" fill="none" stroke="var(--blue)" stroke-width="1.1"><rect x="5" y="2" width="24" height="17" rx="1"/><path d="M1 21h32l-2 3H3z"/><path d="M11 7h2l2 6h6l1.5-4H14"/><circle cx="16" cy="15" r=".8"/><circle cx="20" cy="15" r=".8"/></svg>
</div>
<div class="abs step" style="left:488px;top:409px"><div class="step-title">Choose the order</div><div class="step-text">Lorem ipsum dolor sit amet,<br>consectetur adipiscing elit.</div></div>

<div class="abs step-icon" style="left:340px;top:471px">
  <svg width="40" height="26" viewBox="0 0 40 26" fill="none" stroke="var(--blue)" stroke-width="1.1"><rect x="2" y="2" width="24" height="17"/><path d="M26 7h7l5 6v6H26"/><circle cx="9" cy="21" r="2.5"/><circle cx="31" cy="21" r="2.5"/><circle cx="14" cy="10" r="4.5"/><path d="M12.5 7.5v5h1.5a2.5 2.5 0 0 0 0-5z"/></svg>
</div>
<div class="abs step right" style="left:212px;top:487px;width:120px"><div class="step-title">We deliver</div><div class="step-text">Lorem ipsum dolor sit amet,<br>consectetur adipiscing elit.</div></div>

<div class="abs step-icon" style="left:410px;top:549px">
  <svg width="32" height="28" viewBox="0 0 32 28" fill="none" stroke="var(--blue)" stroke-width="1.1"><path d="M8 16a10 10 0 0 1 20 0z"/><path d="M6 16h24"/><circle cx="18" cy="4.5" r="1.5"/><path d="M2 18h4v8H2zM6 19h6l5 2h5l-1 3H6"/></svg>
</div>
<div class="abs step" style="left:488px;top:565px"><div class="step-title">You enjoy</div><div class="step-text">Lorem ipsum dolor sit amet,<br>consectetur adipiscing elit.</div></div>

<div class="abs btn" style="left:368px;top:640px">LEARN MORE</div>

<div class="abs food" role="img" aria-label="Close-up photo of a fresh salad topped with grilled shrimp"></div>
<section class="abs love">
  <h2>WHY YOU WILL LOVE OUR SHRIMPS</h2>
  <p>Lorem ipsum dolor sit amet, consectetur adipiscing elit. Suspendisse mollis sit amet ligula vit ae commodo.</p>
  <p>Pellentesque habitant morbi tristique senectus et netus et malesuada fames ac turpis egestas. Ut viverra consequat venenatis. Vestibulum scelerisque, lacus a pulvinar condimentum, nisi orci luctus dui, at molestie libero quam sit amet enim. Vivamus dictum venenatis tincidunt.</p>
  <p>Morbi viverra arcu ac quam pharetra egestas. Sed consequat lacus sed mauris fermentum ultricies. Pellentesque id neque magna. Ut et mi sed sem maximus rhoncus id eu arcu. Vestibulum volutpat elit sapien, ut cursus massa congue laoreet.</p>
  <p>Pellentesque habitant morbi tristique senectus et netus et malesuada fames ac turpis egestas.</p>
</section>

<h2 class="abs section-title" style="top:931px">WHAT OUR CUSTOMERS ARE SAYING</h2>
<span class="abs arrow" style="left:162px">&lt;</span>
<span class="abs arrow" style="left:647px">&gt;</span>

<div class="abs review" style="left:184px">
  <div class="stars"><svg width="72" height="12" viewBox="0 0 72 12" fill="var(--star)"><g id="star-row"><path d="M6 0l1.8 3.9 4.2.5-3.1 2.9.8 4.2L6 9.4 2.3 11.5l.8-4.2L0 4.4l4.2-.5z"/><path transform="translate(15)" d="M6 0l1.8 3.9 4.2.5-3.1 2.9.8 4.2L6 9.4 2.3 11.5l.8-4.2L0 4.4l4.2-.5z"/><path transform="translate(30)" d="M6 0l1.8 3.9 4.2.5-3.1 2.9.8 4.2L6 9.4 2.3 11.5l.8-4.2L0 4.4l4.2-.5z"/><path transform="translate(45)" d="M6 0l1.8 3.9 4.2.5-3.1 2.9.8 4.2L6 9.4 2.3 11.5l.8-4.2L0 4.4l4.2-.5z"/><path transform="translate(60)" d="M6 0l1.8 3.9 4.2.5-3.1 2.9.8 4.2L6 9.4 2.3 11.5l.8-4.2L0 4.4l4.2-.5z"/></g></svg></div>
  <div class="review-text">Lorem ipsum dolor sit amet,<br>consectetur adipiscing elit,<br>sed do eiusmod tempor<br>incididunt ut labore et</div>
  <div class="review-name">Dave S</div>
</div>
<div class="abs review" style="left:350px">
  <div class="stars"><svg width="72" height="12" viewBox="0 0 72 12" fill="var(--star)"><use href="#star-row"/></svg></div>
  <div class="review-text">Lorem ipsum dolor sit amet,<br>consectetur adipiscing elit,<br>sed do eiusmod tempor<br>incididunt ut labore et</div>
  <div class="review-name">Christina</div>
</div>
<div class="abs review" style="left:514px">
  <div class="stars"><svg width="72" height="12" viewBox="0 0 72 12" fill="var(--star)"><use href="#star-row"/></svg></div>
  <div class="review-text">Lorem ipsum dolor sit amet,<br>consectetur adipiscing elit,<br>sed do eiusmod tempor<br>incididunt ut labore et</div>
  <div class="review-name">Karen</div>
</div>
<p class="abs more">See more reviews <span>&#9654;</span></p>

<footer class="abs footer">
  <div class="abs foot-links">Home<br>How it works<br>Menu<br>About</div>
  <div class="abs social">
    <div class="foot-title">Follow our Social Media</div>
    <div class="social-row">
      <span class="social-item">Snapgrid</span>
      <span class="social-item">Facelink</span>
      <span class="social-item">Chirper</span>
    </div>
  </div>
  <div class="abs contact"><div class="foot-title">Contact</div><p>Lorem ipsum dolor sit amet, consectetur adipiscing elit,</p></div>
</footer>
<div class="abs bottom">
  <span class="abs" style="left:158px;top:9px">© 2019 Pelican Crest.</span>
  <span class="abs" style="left:614px;top:7px">Privacy</span>
  <span class="abs" style="left:644px;top:7px">Terms</span>
</div>
</body>
</html>
```